Flyer-Design für IT-Dienstleister und Systemhaus
Vielen Dank für die gute Arbeit! Wir sind von dem Resultat begeistert und freuen uns, dass die Zusammenarbeit so angenehm und schnell verlaufen ist.
Zielgruppe
Wir sind ein junger IT-Dienstleister und Systemhaus mit Fokus auf kleine und mittelständische Kunden. Unsere Kunden schätzen unsere hochwertige Arbeitsqualität, unsere Innovationsfähigkeit und Verlässlichkeit.
Aufgabenstellung
Zur (kurzen) Vorstellung unseres Unternehmens und unserer Dienstleistungen, möchten wir einen Falzflyer (Mittelfalz) erstellen. Die gewünschten Abmessungen finden Sie am Ende des Briefings.
Wir wünschen uns ein modernes, gut strukturiertes Layout und einen minimalistischen, dennoch hochwertigen Hintergrund für den Flyer. Aus unserer bisherigen Erfahrung wissen wir, dass die Auswahl von passenden Bildmaterial sehr herausfordernd sein kann – wir würden uns daher wünschen, wenn die Gestaltung des Flyer auch mit wenig Bildmaterial auskommt und Texte gut in Szene setzen kann. Geplant sind zwei Texe mit ca. 200-300 Worten, drei Texte mit ca. 100-200 Worten, sowie ein Unternehmensporträt in variabler Länge.
Unsere Hausschrift ist Open Sans und die Hauptakzentfarbe ist ein dunkles rot. (CMYK 19/100/99/10). In bisherigen Materialien setzen wir auf klare Formen und Linien.
DIN A4, 4-seiter, Endformat: 42,0 cm x 29,7 cm
gefalztes Endformat: 21,0 cm x 29,7 cm
Datenformat: 42,6 cm x 30,3 cm
Falz von links nach rechts in mm: 210

```html
<!DOCTYPE html>
<html lang="de">
<head>
<meta charset="utf-8">
<title>KPLOR GmbH – Falzflyer</title>
<link href="https://fonts.googleapis.com/css2?family=Open+Sans:wght@400;600;700;800&display=swap" rel="stylesheet">
<style>
  :root {
    --red: #b5161b;
    --red-dark: #9c1015;
    --white: #fafafa;
    --paper-grey: #ececec;
    --ink: #2b2b2b;
    --grey: #6d6d6d;
    --stage: #d8d8db;
    --photo-blue-a: #1d2f57;
    --photo-blue-b: #5d7fb0;
    --photo-office-a: #c9ced6;
    --photo-office-b: #5a6f8e;
  }
  * { margin: 0; padding: 0; box-sizing: border-box; }
  html, body { width: 1200px; height: 2515px; overflow: hidden; }
  body {
    background: var(--stage);
    font-family: "Open Sans", Arial, sans-serif;
    color: var(--ink);
    position: relative;
  }
  .spread {
    position: absolute;
    left: 40px;
    width: 1120px;
    height: 792px;
    display: flex;
    box-shadow: 0 20px 50px rgba(0,0,0,.18);
  }
  .spread--outside { top: 385px; }
  .spread--inside { top: 1337px; }
  .page { position: relative; width: 560px; height: 792px; overflow: hidden; background: var(--white); }
  .spread::after {
    content: ""; position: absolute; left: 559px; top: 0; width: 2px; height: 100%;
    background: linear-gradient(90deg, rgba(0,0,0,.12), rgba(255,255,255,.15));
  }
  .band-red { position: absolute; left: 0; right: 0; background: var(--red); }
  .quote-mark { color: var(--red); font-weight: 800; font-size: 1.25em; letter-spacing: -2px; margin-right: 8px; }
  .heading {
    font-weight: 800; text-transform: uppercase; line-height: 1.08; letter-spacing: .5px;
  }
  .body-copy { font-size: 9.5px; line-height: 1.45; text-align: justify; hyphens: auto; }

  /* back page */
  .back-invite { position: absolute; top: 60px; left: 190px; width: 300px; }
  .back-invite .heading { color: var(--red); font-size: 22px; text-align: center; }
  .back-invite .body-copy { margin-top: 36px; color: var(--ink); }
  .back-band { top: 470px; bottom: 0; background: var(--red-dark); }
  .brand-name { font-weight: 400; letter-spacing: -1px; display: flex; align-items: center; gap: 10px; }
  .brand-square { display: inline-block; background: var(--red); }
  .back-band .brand-name { position: absolute; left: 300px; top: 70px; color: var(--white); font-size: 30px; }
  .back-band .brand-square { width: 22px; height: 22px; background: var(--white); }
  .imprint { position: absolute; left: 240px; top: 150px; color: var(--white); font-size: 9.5px; line-height: 1.5; }
  .imprint p + p { margin-top: 10px; }

  /* front page */
  .front-brand { position: absolute; top: 240px; left: 130px; color: var(--grey); font-size: 54px; }
  .front-brand .brand-square { width: 40px; height: 40px; }
  .front-brand small { font-size: 16px; align-self: flex-end; margin-bottom: 8px; letter-spacing: 0; }
  .front-band { top: 400px; bottom: 0; }
  .front-band .heading { position: absolute; right: 40px; bottom: 60px; color: var(--white); font-size: 27px; text-align: right; }

  /* inside left */
  .photo { position: absolute; }
  .photo--team { left: 0; top: 0; width: 1120px; height: 340px;
    background: linear-gradient(135deg, var(--photo-blue-a), var(--photo-blue-b) 60%, #a9c1e2); }
  .intro { position: absolute; top: 380px; left: 50px; width: 460px; display: grid; grid-template-columns: 1fr 1fr; gap: 22px; }
  .intro .lead { grid-column: 1 / -1; font-weight: 700; font-size: 10px; line-height: 1.45; }

  /* inside right */
  .service-band { top: 110px; height: 330px; padding: 40px 44px 0 50px; }
  .service-band .heading { color: var(--white); font-size: 21px; }
  .service-band .heading .quote-mark { color: var(--white); }
  .service-cols { margin-top: 26px; display: grid; grid-template-columns: 1fr 1fr; gap: 22px; color: var(--white); }
  .photo--office { left: 0; top: 440px; width: 560px; height: 352px;
    background: linear-gradient(160deg, var(--photo-office-a), #9fb0c6 50%, var(--photo-office-b)); }
  .partner-claim { position: absolute; right: 40px; bottom: 46px; color: var(--red); font-size: 19px; text-align: right; }
  .partner-claim .quote-mark { margin: 0 0 0 8px; }
</style>
</head>
<body>

<section class="spread spread--outside">
  <article class="page page--back">
    <div class="back-invite">
      <h2 class="heading"><span class="quote-mark">”</span>Wir freuen<br>uns auf Sie!</h2>
      <p class="body-copy">Sie haben weitere Fragen zum Thema IT und unseren Leistungen als Systemhaus? Nehmen Sie einfach und unverbindlich Kontakt zu uns auf! Wir freuen uns auf Sie und zeigen Ihnen, wie die Kooperation mit einem professionellen IT-Dienstleister mit einem klugen IT-Workplace Management die Qualität Ihrer Unternehmens-IT und die damit verbundenen Kosten kurz- und langfristig positiv beeinflussen kann. Zögern Sie nicht und meistern Sie mit uns gemeinsam die digitalen Herausforderungen von Gegenwart und Zukunft!</p>
    </div>
    <div class="band-red back-band">
      <div class="brand-name"><span class="brand-square"></span>KPLOR GmbH</div>
      <div class="imprint">
        <p>KPLOR GmbH<br>Talweg 7<br>78112 Mühlbach</p>
        <p>Telefon: +49 (0)7400 12345<br>Telefax: +49 (0)7400 12345 99<br>E-Mail: info@kplor.com</p>
        <p>Geschäftsführer: Lena Hartwig</p>
        <p>Registergericht: Amtsgericht Mühlbach<br>Registernummer: HRB 481920</p>
      </div>
    </div>
  </article>
  <article class="page page--front">
    <div class="brand-name front-brand"><span class="brand-square"></span>KPLOR<small>GmbH</small></div>
    <div class="band-red front-band">
      <h1 class="heading">Vielseitiger<br>IT-Dienstleister<br>im Full-Service</h1>
    </div>
  </article>
</section>

<section class="spread spread--inside">
  <div class="photo photo--team" role="img" aria-label="Foto: zwei Fachleute im Rechenzentrum mit Tablet und eingeblendeten Cloud-Symbolen"></div>
  <article class="page page--intro" style="background:transparent">
    <div class="intro" style="top:380px">
      <p class="lead">Die KPLOR GmbH ist ein junges Systemhaus und IT-Dienstleister mit Sitz in Mühlbach. Wir begleiten kleine und mittelständische Unternehmen mit durchdachten Lösungen, verlässlichem Service und persönlicher Beratung – vom ersten Gespräch bis zum laufenden Betrieb Ihrer gesamten IT-Umgebung.</p>
      <p class="body-copy">Kleine und mittelständische Firmen stehen heute vor denselben digitalen Aufgaben wie große Konzerne, verfügen aber selten über eine eigene IT-Abteilung. Genau hier setzen wir an. Wir übernehmen Planung, Einrichtung und Pflege Ihrer Systeme, damit Sie sich voll auf Ihr Kerngeschäft konzentrieren können. Als erfahrenes Team wissen wir, wie wichtig schnelle Reaktionszeiten und klare Ansprechpartner sind, und richten unsere Arbeit konsequent danach aus.</p>
      <p class="body-copy">Unsere Leistungen reichen von der Beschaffung moderner Hardware über sichere Netzwerke bis hin zu Cloud-Diensten und Datensicherung. Dabei setzen wir auf bewährte Technik und transparente Abläufe. Gemeinsam mit Ihnen entwickeln wir eine IT, die mit Ihrem Unternehmen wächst, zuverlässig läuft und sich an neue Anforderungen flexibel anpassen lässt. So entsteht eine Partnerschaft auf Augenhöhe, die Ihnen dauerhaft Sicherheit und Freiraum verschafft.</p>
    </div>
  </article>
  <article class="page page--services" style="background:transparent">
    <div class="band-red service-band">
      <h2 class="heading"><span class="quote-mark">”</span>Beratung und<br>Konzeption für<br>einen effizienten<br>Betrieb</h2>
      <div class="service-cols">
        <p class="body-copy">Jedes Unternehmen ist anders, was Bedarf und Erwartungshaltung an den IT-Workplace anbelangt. Wir sind hier mit einer ausführlichen Beratung auf Ihrer Seite und ermitteln gemeinsam mit Ihnen, welche Lösungen für Ihren Alltag wirklich sinnvoll sind und wo Potenzial für Verbesserungen liegt.</p>
        <p class="body-copy">Auf dieser Grundlage erstellen wir ein klares Konzept für den effizienten Betrieb Ihrer IT-Landschaft. Es ist auf Ihre Branche, die Größe Ihres Unternehmens und Ihre Mitarbeiterstruktur zugeschnitten und bleibt dabei jederzeit erweiterbar.</p>
      </div>
    </div>
    <div class="photo photo--office" role="img" aria-label="Foto: zwei Mitarbeiter besprechen sich an einem Arbeitsplatz im Büro"></div>
    <h2 class="heading partner-claim">Starker Partner für<br>kleine Firmen und<br>den Mittelstand<span class="quote-mark">”</span></h2>
  </article>
</section>

</body>
</html>
```